San Francisco Pet Care Non Profit

Business Card Design for non profit organization.
We are a mobile pet care team who supports and attends to pets whose owners are homeless. Thanks for your help and creativity.

Industry/Entity Type

Non Profit

Contact Information for Business Card

Marisol Keddy
President
2871 Larkmoor Street, #512
San Francisco, CA 94187
phone: 415-729-3846
fax: 415-781-4052
marisol@tidywagonvan.org
website: tidywagonvan.org
facebook: friendloop.com/TidyWagonVan

Font styles to use
Serif
Sans Serif

Colors

Designer to choose colors to be used in the design.

Requirements
Must have
• above details and attached logo

```html
<!DOCTYPE html>
<html lang="en">
<head>
<meta charset="utf-8">
<title>TidyWagonVan Business Card</title>
<link rel="stylesheet" href="https://fonts.googleapis.com/css2?family=Jost:wght@400;500;600&family=Arimo:wght@700&display=swap">
<style>
  :root {
    --stage: #1c1c1c;
    --paper: #ffffff;
    --brand-blue: #1aa7ec;
    --deep-blue: #0a86dc;
    --sky-blue: #8fd0fb;
    --pill-fill: #c6eefe;
    --ink: #1f1f1f;
    --rule: #d4d4d4;
  }
  * { margin: 0; padding: 0; box-sizing: border-box; }
  html, body { width: 1200px; height: 1200px; overflow: hidden; background: var(--stage); }
  body { position: relative; font-family: "Jost", sans-serif; color: var(--ink); }

  .card { position: absolute; left: 174px; width: 840px; height: 480px; background: var(--paper); overflow: hidden; }
  .card--front { top: 103px; }
  .card--back { top: 605px; }

  /* front */
  .front-art { position: absolute; inset: 0; }
  .brand { position: absolute; display: flex; align-items: center; gap: 10px; }
  .brand__dot { width: 14px; height: 14px; border-radius: 50%; background: var(--brand-blue); }
  .brand__name { font-family: "Jost", sans-serif; font-weight: 600; color: var(--brand-blue); line-height: 1; }
  .tagline { position: absolute; font-family: "Arimo", sans-serif; font-weight: 700; color: var(--ink); line-height: 1; }

  .front-brand { left: 48px; top: 60px; }
  .front-brand .brand__name { font-size: 46px; }
  .front-tagline { left: 171px; top: 114px; font-size: 18px; }

  .name-pill {
    position: absolute; left: -4px; top: 157px; width: 365px; height: 101px;
    background: var(--pill-fill); border: 3px solid var(--brand-blue); border-left: none;
    border-radius: 0 50px 50px 0; padding: 18px 0 0 78px;
  }
  .name-pill__name { font-size: 31px; font-weight: 600; color: var(--brand-blue); line-height: 1.1; }
  .name-pill__role { font-size: 21px; font-weight: 400; margin-top: 6px; }

  .contacts { position: absolute; left: 72px; top: 290px; list-style: none; }
  .contact { position: relative; display: flex; align-items: flex-start; font-size: 21px; line-height: 28px; margin-bottom: 18px; }
  .contact:nth-child(2) { margin-bottom: 14px; }
  .contact__icon { width: 36px; height: 36px; border-radius: 50%; background: var(--brand-blue); flex: none; margin-right: 16px; margin-top: -4px; display: flex; align-items: center; justify-content: center; }
  .contact__label { width: 86px; flex: none; }
  .contact__value { white-space: nowrap; }

  /* back */
  .back-photo { position: absolute; left: 0; top: 0; width: 840px; height: 279px;
    background: linear-gradient(100deg, #f2f2f2 0%, #e4e4e4 30%, #9a6d55 50%, #c77a7a 65%, #e8e6e2 78%, #8a8d90 100%); }
  .back-brand { left: 0; right: 0; top: 314px; justify-content: center; }
  .back-brand .brand__name { font-size: 52px; }
  .back-brand .brand__dot { width: 18px; height: 18px; }
  .back-tagline { left: 0; right: 0; top: 372px; text-align: center; font-size: 22px; padding-left: 80px; }
  .back-rule { position: absolute; left: 0; right: 0; top: 411px; height: 1px; background: var(--rule); }
  .back-footer { position: absolute; left: 72px; right: 50px; top: 428px; display: flex; justify-content: space-between; font-size: 21px; }
  .footer-item { display: flex; align-items: center; gap: 12px; }
  .footer-item strong { font-weight: 600; }
  .globe { width: 27px; height: 27px; border-radius: 50%; background: var(--deep-blue); }
  .square { width: 25px; height: 25px; border-radius: 3px; background: var(--deep-blue); }
</style>
</head>
<body>

<section class="card card--front">
  <svg class="front-art" width="840" height="480" viewBox="0 0 840 480">
    <polygon points="606,0 704,0 502,239 404,239" fill="var(--brand-blue)"/>
    <polygon points="404,239 502,239 690,480 598,480 560,440 530,370" fill="var(--deep-blue)"/>
    <polygon points="470,260 530,300 560,400 600,470 540,420" fill="var(--brand-blue)"/>
    <polygon points="704,0 840,0 840,480 690,480 540,290 502,239" fill="var(--sky-blue)"/>
    <foreignObject x="0" y="0" width="840" height="480">
      <div xmlns="http://www.w3.org/1999/xhtml" role="img" aria-label="Photo of a couple hugging and kissing their white dog"
        style="width:840px;height:480px;clip-path:polygon(704px 0,840px 0,840px 480px,690px 480px,540px 290px,560px 240px);background:linear-gradient(160deg,#8fd0fb 0%,#b07a5e 35%,#c87e84 55%,#e7e2dc 75%,#6b4a3a 100%);"></div>
    </foreignObject>
  </svg>

  <div class="brand front-brand">
    <span class="brand__dot"></span>
    <span class="brand__name">TidyWagonVan</span>
  </div>
  <div class="tagline front-tagline">Mobile Pet Care Team</div>

  <div class="name-pill">
    <div class="name-pill__name">Marisol Keddy</div>
    <div class="name-pill__role">President</div>
  </div>

  <ul class="contacts">
    <li class="contact">
      <span class="contact__icon"><svg width="20" height="20" viewBox="0 0 24 24"><path d="M6.6 10.8a15 15 0 0 0 6.6 6.6l2.2-2.2a1 1 0 0 1 1-.25 11 11 0 0 0 3.6.6 1 1 0 0 1 1 1V20a1 1 0 0 1-1 1A17 17 0 0 1 3 4a1 1 0 0 1 1-1h3.5a1 1 0 0 1 1 1 11 11 0 0 0 .6 3.6 1 1 0 0 1-.25 1z" fill="none" stroke="#fff" stroke-width="1.8"/></svg></span>
      <span class="contact__label">Phone:</span><span class="contact__value">415-729-3846</span>
    </li>
    <li class="contact">
      <span class="contact__icon"><svg width="20" height="20" viewBox="0 0 24 24" fill="none" stroke="#fff" stroke-width="1.8"><rect x="6" y="3" width="12" height="6"/><rect x="3" y="9" width="18" height="8" rx="2"/><rect x="7" y="14" width="10" height="7"/></svg></span>
      <span class="contact__label">Fax:</span><span class="contact__value">415-781-4052</span>
    </li>
    <li class="contact">
      <span class="contact__icon"><svg width="20" height="20" viewBox="0 0 24 24" fill="none" stroke="#fff" stroke-width="1.8"><path d="M12 22s7-7.5 7-13a7 7 0 0 0-14 0c0 5.5 7 13 7 13z"/><circle cx="12" cy="9" r="2.5"/></svg></span>
      <span class="contact__label">Place:</span><span class="contact__value">2871 Larkmoor Street, #512<br>San Francisco, CA 94187</span>
    </li>
  </ul>
</section>

<section class="card card--back">
  <div class="back-photo" role="img" aria-label="Photo of a couple hugging their white dog beside a grey wall"></div>
  <div class="brand back-brand">
    <span class="brand__dot"></span>
    <span class="brand__name">TidyWagonVan</span>
  </div>
  <div class="tagline back-tagline">Mobile Pet Care Team</div>
  <div class="back-rule"></div>
  <div class="back-footer">
    <div class="footer-item"><span class="globe"></span><span><strong>Website</strong>: tidywagonvan.org</span></div>
    <div class="footer-item"><span class="square"></span><span>friendloop.com/TidyWagonVan</span></div>
  </div>
</section>

</body>
</html>
```